I need to refresh my meeting minutes pages (2 of them)

I have 2 pages that need to be modernized with a new look and feel. I have attached the 2 pages that need the refresh. I am okay with one page submissions as long as the winner is willing to add the second page before payment :-) Any questions please let me know. The logo on the page is not ours but a sample of what client may give us.

```html
<!DOCTYPE html>
<html lang="en">
<head>
<meta charset="utf-8">
<title>Agenda Item Details</title>
<link rel="stylesheet" href="https://fonts.googleapis.com/css2?family=Inter:ital,wght@0,400;0,500;0,600;0,700;1,700&display=swap">
<style>
:root{
  --navy:#2d3c4f;
  --teal:#1abc9c;
  --row:#edf0f2;
  --row-line:#dfe4e8;
  --row-text:#6b7580;
  --active:#d3e3ef;
  --active-bar:#2e8fe0;
  --label:#7a8590;
  --white:#ffffff;
  --scroll-track:#e3e6e9;
  --scroll-thumb:#9aa3ab;
}
*{box-sizing:border-box;margin:0;padding:0}
html,body{width:1200px;height:989px;overflow:hidden;font-family:"Inter",sans-serif;background:var(--white)}
.topbar{position:absolute;left:0;top:0;width:1200px;height:58px;background:var(--navy);display:flex;align-items:center;justify-content:space-between;padding:0 35px}
.brand{color:var(--white);font-weight:700;font-size:20px;letter-spacing:.5px}
.nav{display:flex;gap:30px}
.nav a{color:var(--white);text-decoration:none;font-size:13.5px;font-weight:500;letter-spacing:.3px;position:relative}
.nav a.current{font-weight:700}
.nav a.current::after{content:"";position:absolute;left:0;right:0;bottom:-6px;height:2px;background:var(--white)}
.sidebar{position:absolute;left:0;top:58px;width:376px;height:873px;background:var(--row);overflow:hidden}
.search{position:absolute;left:15px;top:17px;width:346px;height:42px;border:1px solid #8a939b;border-radius:6px;background:var(--white);display:flex;align-items:center;justify-content:space-between;padding:0 14px 0 18px;color:#6b7580;font-size:15px}
.agenda-list{position:absolute;left:0;top:75px;width:367px;list-style:none}
.agenda-list li{display:flex;align-items:center;justify-content:space-between;padding:0 22px 0 34px;border-bottom:1px solid var(--row-line);color:var(--row-text);font-size:15px;height:58px;line-height:1.8}
.agenda-list li.section{background:var(--teal);color:var(--white);font-size:18.5px;border-bottom:none;white-space:nowrap}
.agenda-list li.tall{height:83px}
.agenda-list li.small{font-size:13.5px}
.agenda-list li.active{background:var(--active);color:var(--navy);font-weight:700;box-shadow:inset 4px 0 0 var(--active-bar)}
.agenda-list svg{flex:none}
.scrollbar{position:absolute;left:367px;top:75px;width:9px;height:798px;background:var(--scroll-track)}
.scrollbar span{position:absolute;left:1px;top:0;width:7px;height:167px;background:var(--scroll-thumb);border-radius:4px}
.hero{position:absolute;left:409px;top:87px;width:758px;height:385px;border-radius:27px;overflow:hidden}
.hero-photo{position:absolute;inset:0;background:linear-gradient(135deg,#6f7b86 0%,#9aa4ad 40%,#b5bcc3 60%,#7b8590 100%)}
.hero-shade{position:absolute;inset:0;background:rgba(45,60,79,.25)}
.hero h1{position:absolute;left:0;right:0;top:134px;text-align:center;color:var(--white);font-size:38px;font-weight:700}
.share{position:absolute;left:711px;top:26px}
.download{position:absolute;left:197px;top:221px;width:363px;height:99px;border:2px solid var(--white);border-radius:7px;color:var(--white);font-size:13.5px;display:flex;flex-direction:column;align-items:center;justify-content:center;gap:14px}
.details-title{position:absolute;left:409px;top:496px;font-size:38px;font-style:italic;font-weight:700;color:var(--navy)}
.pager{position:absolute;left:1079px;top:493px;display:flex;gap:4px}
.pager span{width:42px;height:42px;background:#e6eaed;border-radius:6px;display:flex;align-items:center;justify-content:center}
.details{position:absolute;left:409px;top:551px;font-size:15px;color:var(--label)}
.details div{display:flex;height:43.5px;align-items:center}
.details dt{width:158px}
.footer{position:absolute;left:0;top:931px;width:1200px;height:58px;background:var(--navy);color:var(--white);font-size:13.5px;display:flex;align-items:center;padding-left:34px}
</style>
</head>
<body>
<header class="topbar">
  <div class="brand">NWSD</div>
  <nav class="nav">
    <a href="#">FEATURED</a>
    <a href="#">MEETINGS</a>
    <a href="#" class="current">AGENDA</a>
    <a href="#">POLICIES</a>
  </nav>
</header>

<aside class="sidebar">
  <div class="search">Search Meetings ...
    <svg width="20" height="20" viewBox="0 0 20 20" fill="none" stroke="#6b7580" stroke-width="2"><circle cx="8" cy="8" r="6"/><path d="M12.5 12.5L18 18"/></svg>
  </div>
  <ul class="agenda-list">
    <li class="section">*R* WELCOME</li>
    <li>Wireless Access For Guests</li>
    <li class="section">*R* CALL TO ORDER</li>
    <li>Pledge Of Allegiance</li>
    <li>Roll Call</li>
    <li class="section">RIDGEVIEW PROUD</li>
    <li>Lakeside Hockey Coach <svg width="18" height="22" viewBox="0 0 18 22" fill="none" stroke="#6b7580" stroke-width="1.6"><path d="M2 1h9l5 5v15H2z"/><path d="M5 11h8M5 14h8M5 17h8"/></svg></li>
    <li class="tall"><span>Teaching Professions - Future<br>Teachers State Competition</span> <svg width="18" height="22" viewBox="0 0 18 22" fill="none" stroke="#6b7580" stroke-width="1.6"><path d="M2 1h9l5 5v15H2z"/><path d="M5 11h8M5 14h8M5 17h8"/></svg></li>
    <li class="section">*R* INFORMATION TO THE BOARD</li>
    <li class="small">Superintendent - ACES/PAGE/First Step</li>
    <li>ACES <svg width="18" height="22" viewBox="0 0 18 22" fill="none" stroke="#6b7580" stroke-width="1.6"><path d="M2 1h9l5 5v15H2z"/><path d="M5 11h8M5 14h8M5 17h8"/></svg></li>
    <li class="active">PAGE <svg width="18" height="22" viewBox="0 0 18 22" fill="none" stroke="#2d3c4f" stroke-width="1.8"><path d="M2 1h9l5 5v15H2z"/><path d="M5 11h8M5 14h8M5 17h8"/></svg></li>
    <li>First Step <svg width="18" height="22" viewBox="0 0 18 22" fill="none" stroke="#6b7580" stroke-width="1.6"><path d="M2 1h9l5 5v15H2z"/><path d="M5 11h8M5 14h8M5 17h8"/></svg></li>
    <li></li>
  </ul>
  <div class="scrollbar"><span></span></div>
</aside>

<section class="hero">
  <div class="hero-photo" role="img" aria-label="Blurred photo of hands writing with a pen on a spiral notebook"></div>
  <div class="hero-shade"></div>
  <svg class="share" width="22" height="22" viewBox="0 0 22 22" fill="#fff" stroke="#fff" stroke-width="1.6"><circle cx="17" cy="4" r="2.6"/><circle cx="5" cy="11" r="2.6"/><circle cx="17" cy="18" r="2.6"/><path d="M7 10l8-5M7 12l8 5" fill="none"/></svg>
  <h1>Agenda Item Details</h1>
  <div class="download">
    <svg width="18" height="18" viewBox="0 0 18 18" fill="none" stroke="#fff" stroke-width="2"><path d="M9 1v10M4 7l5 5 5-5M1 16h16"/></svg>
    <span>2025-04-10 - Ridgeview Proud - PAGE (1).pdf (40 KB)</span>
  </div>
</section>

<h2 class="details-title">Agenda Item Details</h2>
<div class="pager">
  <span><svg width="12" height="20" viewBox="0 0 12 20" fill="none" stroke="#5b6670" stroke-width="2"><path d="M10 2L2 10l8 8"/></svg></span>
  <span><svg width="12" height="20" viewBox="0 0 12 20" fill="none" stroke="#5b6670" stroke-width="2"><path d="M2 2l8 8-8 8"/></svg></span>
</div>
<dl class="details">
  <div><dt>Meeting</dt><dd>Apr 10, 2025 - Regular Meeting Agenda</dd></div>
  <div><dt>Category</dt><dd>*R* INFORMATION TO THE BOARD</dd></div>
  <div><dt>Subject</dt><dd>PAGE</dd></div>
  <div><dt>Type</dt><dd></dd></div>
</dl>

<footer class="footer">MeetingDeskR A Keystone Brand, © 2002-2025</footer>
</body>
</html>
```